i need a business card design for my family investment company "norvane holdings" based in dubai. its a diverse investment firm focusing on education, hospitality and automotive. the design has to be modern and try to incorporate the logo "E" in the design. details on card as follow

Tariq H Bin Rashoud
Managing Director
tariq@norvane.ae
www.norvane.ae

Harbor park,palmcrest tower, office 1730, dubai
tel. 04 3819025
mobile.050 4172958

Target Market(s)

card used for networking events and investor meetings

Industry/Entity Type

Hospitality

```html
<!DOCTYPE html>
<html lang="en">
<head>
<meta charset="utf-8">
<title>Norvane Holdings — Business Card</title>
<link href="https://fonts.googleapis.com/css2?family=Open+Sans:wght@300;400;700&display=swap" rel="stylesheet">
<style>
  :root {
    --backdrop: #efefef;
    --card: #ffffff;
    --brand-blue: #376695;
    --ink: #141414;
    --on-blue: #ffffff;
    --card-w: 540px;
    --card-h: 309px;
  }
  * { box-sizing: border-box; margin: 0; padding: 0; }
  html, body {
    width: 1200px; height: 720px; overflow: hidden;
    background: var(--backdrop);
    font-family: "Open Sans", sans-serif;
  }
  .sheet { position: relative; width: 1200px; height: 720px; }
  .card {
    position: absolute; top: 205px;
    width: var(--card-w); height: var(--card-h);
    background: var(--card);
    box-shadow: 0 2px 6px rgba(0,0,0,.12);
    overflow: hidden;
  }
  .card--back { left: 40px; }
  .card--front { left: 620px; }

  /* Back */
  .back-name {
    position: absolute; left: 0; right: 0; top: 128px;
    text-align: center;
    font-weight: 300; font-size: 30px; letter-spacing: 8px;
    text-transform: uppercase; color: var(--brand-blue);
  }
  .back-web {
    position: absolute; right: 36px; bottom: 30px;
    font-size: 13px; font-weight: 400; color: var(--brand-blue);
  }

  /* Front */
  .front-shape { position: absolute; inset: 0; }
  .wordmark {
    position: absolute; left: 30px; top: 58px;
    display: flex; align-items: center; gap: 12px;
  }
  .wordmark-square { width: 12px; height: 12px; background: var(--brand-blue); flex: none; }
  .wordmark-name {
    font-weight: 300; font-size: 20px; line-height: 26px; letter-spacing: 6px;
    text-transform: uppercase; color: var(--ink);
  }
  .wordmark-name span { display: block; }
  .details {
    position: absolute; right: 24px; top: 70px;
    text-align: right; color: var(--on-blue);
  }
  .person-name { font-weight: 700; font-size: 14px; }
  .person-role { font-size: 11.5px; color: var(--ink); margin-top: 1px; }
  .contact-list { list-style: none; margin-top: 28px; font-size: 11.5px; line-height: 18px; }
  .contact-list li { display: flex; justify-content: flex-end; align-items: flex-start; gap: 8px; }
  .contact-list .spaced { margin-top: 6px; }
  .icon { width: 12px; height: 12px; flex: none; margin-top: 3px; }
</style>
</head>
<body>
<main class="sheet">

  <section class="card card--back" aria-label="Card back">
    <p class="back-name">Norvane Holdings</p>
    <p class="back-web">www.norvane.ae</p>
  </section>

  <section class="card card--front" aria-label="Card front">
    <svg class="front-shape" width="540" height="309" viewBox="0 0 540 309" aria-hidden="true">
      <path d="M250 0 Q214 160 262 309 L270 309 Q228 150 292 0 Z" fill="var(--ink)"/>
      <path d="M292 0 Q228 150 270 309 L540 309 L540 0 Z" fill="var(--brand-blue)"/>
    </svg>

    <div class="wordmark">
      <span class="wordmark-square"></span>
      <p class="wordmark-name"><span>Norvane</span><span>Holdings</span></p>
    </div>

    <div class="details">
      <p class="person-name">Tariq H Bin Rashoud</p>
      <p class="person-role">Managing Director</p>
      <ul class="contact-list">
        <li>tariq@norvane.ae
          <svg class="icon" viewBox="0 0 12 12"><rect x="0.5" y="2" width="11" height="8" fill="none" stroke="var(--ink)"/><path d="M0.5 2 L6 6.5 L11.5 2" fill="none" stroke="var(--ink)"/></svg>
        </li>
        <li class="spaced">050 4172958
          <svg class="icon" viewBox="0 0 12 12"><rect x="3" y="0.5" width="6" height="11" rx="1" fill="none" stroke="var(--ink)"/><rect x="4.2" y="2" width="3.6" height="5" fill="var(--ink)"/></svg>
        </li>
        <li>04 3819025
          <svg class="icon" viewBox="0 0 12 12"><path d="M1 4 Q6 0 11 4 L9.5 5.5 L8 4.3 L4 4.3 L2.5 5.5 Z" fill="var(--ink)"/><rect x="2.5" y="6" width="7" height="5" rx="1" fill="var(--ink)"/></svg>
        </li>
        <li class="spaced">Harbor park,palmcrest tower,<br>office 1730, dubai
          <svg class="icon" viewBox="0 0 12 12"><path d="M6 11.5 Q1.5 6.5 1.5 4.5 A4.5 4.5 0 0 1 10.5 4.5 Q10.5 6.5 6 11.5 Z" fill="var(--ink)"/><circle cx="6" cy="4.5" r="1.6" fill="var(--brand-blue)"/></svg>
        </li>
      </ul>
    </div>
  </section>

</main>
</body>
</html>
```